Landing Page Design für Ankauf-Shop von Metall (Schrott)
Zielgruppe
Ankauf Shop für Metall (Schrott) Versand mittels Paketversand.
Der Shop ist bereits vorhanden unter flinkmetall.de
Gesucht wird eine ansprechende Landing Page
Logo und Logofarbe sind bereits fest. ( siehe flinkmetall.de)
Footer muss nicht dabei sein, ein Textfeld mit dem Begriff „wie gehts“ muss vorhanden sein, damit der Kundschaft erklärt werden kann, wie der Ablauf ist.
Das Design wird benötig für Desktop, Tablet und Smartphone.
Aufgabenstellung
Klarheit, Übersichtlichkeit, ansprechendes Design,

```html
<!DOCTYPE html>
<html lang="de">
<head>
<meta charset="utf-8">
<title>flinkmetall.de – Metall online verkaufen</title>
<link href="https://fonts.googleapis.com/css2?family=Open+Sans:wght@300;400;600;700;800&display=swap" rel="stylesheet">
<style>
  :root{
    --green:#7cb82f;
    --white:#ffffff;
    --grey:#666666;
    --copper-dark:#a8401f;
    --copper-mid:#d9805c;
    --copper-light:#e9c2b0;
    --sky:#cfd6dc;
  }
  *{margin:0;padding:0;box-sizing:border-box;}
  html,body{width:1108px;height:1200px;overflow:hidden;}
  body{font-family:"Open Sans",sans-serif;background:var(--white);position:relative;}

  .site-header{position:absolute;left:0;top:0;width:1108px;height:92px;background:var(--green);}
  .brand{position:absolute;left:114px;top:30px;display:flex;align-items:center;gap:8px;color:var(--white);font-weight:700;font-size:19px;text-decoration:none;}
  .brand-dot{width:30px;height:30px;border-radius:50%;background:var(--white);}
  .main-nav a{position:absolute;top:36px;color:var(--white);font-weight:700;font-size:13px;text-decoration:none;}

  .hero{position:absolute;left:0;top:92px;width:1108px;height:606px;}
  .hero-photo{position:absolute;inset:0;
    background:
      radial-gradient(ellipse 420px 220px at 300px 60px, var(--sky) 0%, rgba(207,214,220,0) 100%),
      radial-gradient(ellipse 500px 300px at 850px 380px, var(--copper-light) 0%, rgba(233,194,176,0) 100%),
      linear-gradient(120deg, var(--copper-mid) 0%, var(--copper-dark) 45%, var(--copper-mid) 75%, var(--copper-light) 100%);}
  .feature{position:absolute;top:143px;width:225px;height:165px;background:var(--white);text-align:center;}
  .feature svg{position:absolute;left:50%;top:36px;transform:translateX(-50%);}
  .feature-title{position:absolute;left:0;right:0;top:116px;font-size:19.5px;color:var(--green);font-weight:300;white-space:nowrap;}
  .feature-title strong{font-weight:800;}
  .cta{position:absolute;left:447px;top:414px;width:214px;height:71px;background:var(--green);border-radius:3px;color:var(--white);font-weight:700;font-size:16.5px;display:flex;align-items:center;justify-content:center;text-decoration:none;}

  .how{position:absolute;left:0;top:698px;width:1108px;height:502px;background:var(--white);}
  .how-shape{position:absolute;left:0;top:0;}
  .how-title{position:absolute;left:114px;top:26px;font-size:46px;font-weight:700;color:var(--white);}
  .how-text{position:absolute;left:114px;top:110px;width:370px;font-size:16.5px;line-height:25px;color:var(--white);}
  .how-text p + p{margin-top:25px;}

  .slogan{position:absolute;left:642px;top:82px;width:400px;text-align:center;font-size:63px;line-height:75px;}
  .slogan .light{display:block;font-weight:300;color:var(--grey);}
  .slogan .bold{display:block;font-weight:800;color:var(--green);}
  .slogan-badge{position:absolute;left:688px;top:326px;width:305px;height:65px;background:var(--green);border-radius:12px;color:var(--white);font-weight:700;font-size:48px;line-height:65px;text-align:center;}
</style>
</head>
<body>
  <header class="site-header">
    <a class="brand" href="#"><span class="brand-dot"></span>flinkmetall.de</a>
    <nav class="main-nav">
      <a href="#" style="left:599px">Startseite</a>
      <a href="#" style="left:692px">Metalle verkaufen</a>
      <a href="#" style="left:845px">Über uns</a>
      <a href="#" style="left:940px">Kontakt</a>
    </nav>
  </header>

  <section class="hero">
    <div class="hero-photo" role="img" aria-label="Unscharfes Foto von gebündelten Kupferkabeln"></div>

    <div class="feature" style="left:118px">
      <svg width="68" height="46" viewBox="0 0 68 46" fill="none" stroke="#7cb82f" stroke-width="3" stroke-linecap="round" stroke-linejoin="round">
        <path d="M14 4h30v30H14"/><path d="M44 14h12l8 10v10h-6"/><path d="M44 34h6"/>
        <circle cx="22" cy="36" r="5"/><circle cx="54" cy="36" r="5"/>
        <path d="M2 12h8M4 20h8M2 28h8M14 36h3"/>
      </svg>
      <div class="feature-title"><strong>Einfacher</strong> Versand</div>
    </div>

    <div class="feature" style="left:441px">
      <svg width="70" height="56" viewBox="0 0 70 56" fill="none" stroke="#7cb82f" stroke-width="3" stroke-linecap="round">
        <circle cx="44" cy="32" r="20"/><path d="M38 6h12M44 6v6M60 12l4-4M28 12l-4-4"/>
        <path d="M44 22v12"/><circle cx="44" cy="34" r="1.5" fill="#7cb82f"/>
        <path d="M4 24h14M2 32h14M6 40h12"/>
      </svg>
      <div class="feature-title"><strong>Schnelle</strong> Auszahlung</div>
    </div>

    <div class="feature" style="left:764px">
      <svg width="56" height="56" viewBox="0 0 56 56" fill="none" stroke="#7cb82f" stroke-width="3" stroke-linecap="round" stroke-linejoin="round">
        <path d="M8 22A21 21 0 0 1 46 14"/><path d="M46 6v8h-8"/>
        <path d="M48 34A21 21 0 0 1 10 42"/><path d="M10 50v-8h8"/>
        <text x="28" y="36" text-anchor="middle" font-family="Open Sans, sans-serif" font-weight="800" font-size="22" fill="#7cb82f" stroke="none">$</text>
      </svg>
      <div class="feature-title"><strong>Aktuelle</strong> Preise</div>
    </div>

    <a class="cta" href="#">Zum verkauf</a>
  </section>

  <section class="how">
    <svg class="how-shape" width="1108" height="502" viewBox="0 0 1108 502" aria-hidden="true">
      <defs>
        <filter id="edge-shadow" x="-10%" y="-10%" width="120%" height="120%">
          <feDropShadow dx="6" dy="0" stdDeviation="6" flood-color="#000" flood-opacity="0.18"/>
        </filter>
      </defs>
      <path d="M0 0H487C505 180 600 330 743 502H0Z" fill="#7cb82f" filter="url(#edge-shadow)"/>
    </svg>

    <h2 class="how-title">So geht‘s !</h2>
    <div class="how-text">
      <p>Lorem ipsum dolor sit amet, consectetur adipisicing elit, sed do eiusmod tempor incididunt ut labore et dolore magna aliqua. Ut enim ad minim veniam, quis nostrud exercitation ullamco laboris nisi ut aliquip ex ea commodo consequat.</p>
      <p>&nbsp;Duis aute irure dolor in reprehenderit in voluptate velit esse cillum dolore eu fugiat nulla pariatur. Excepteur sint occaecat cupidatat non proident, sunt in culpa qui officia deserunt mollit anim id est laborum.</p>
    </div>

    <div class="slogan">
      <span class="light">Online</span>
      <span class="bold">flink</span>
      <span class="light">Metall</span>
    </div>
    <div class="slogan-badge">verkaufen</div>
  </section>
</body>
</html>
```